Stationery and Business Card for Exporter
Brennor Global
Stationery and Business Card for Exporter - Manufacturing
Kiran Velur
CEO
112 Kovirath Industrial Estate, Tarunpeth, Ahmedabad 380119. India
info@brennorglbl.com
www.brennorglbl.com
Below Title, please put follwing: M.S. Industrial Engineering (USA)

```html
<!DOCTYPE html>
<html lang="en">
<head>
<meta charset="utf-8">
<title>Brennor Global — Stationery Concepts</title>
<link rel="stylesheet" href="https://fonts.googleapis.com/css2?family=Montserrat:wght@500;700&family=Open+Sans:wght@400;600&family=Great+Vibes&display=swap">
<style>
:root{
  --navy:#2b2a86;
  --gold:#c9a548;
  --paper:#ffffff;
  --stage:#3b3b3b;
  --ink:#555;
  --rule:#d8d8e4;
}
*{box-sizing:border-box;margin:0;padding:0}
html,body{width:1200px;height:254px;overflow:hidden;background:var(--stage)}
body{position:relative;font-family:'Open Sans',sans-serif;color:var(--ink)}
.piece{position:absolute;background:var(--paper);overflow:hidden}
.piece.navy{background:var(--navy)}
.piece.gold{background:var(--gold)}
.caption{position:absolute;font-size:2.4px;color:#cfcfcf;text-align:center;width:100%;bottom:-5px;left:0}
.wordmark{font-family:'Montserrat',sans-serif;font-weight:700;color:var(--navy);letter-spacing:.06em;white-space:nowrap;text-transform:uppercase}
.navy .wordmark{color:#fff}
.gold .wordmark{color:#fff}
.center{position:absolute;left:0;right:0;text-align:center}
.tiny{font-size:1.9px;line-height:2.6px;color:#777}
.navy .tiny{color:#dcdcf0}
.intro{position:absolute;left:30px;top:34px;width:52px;text-align:center;color:#fff}
.intro .wordmark{color:#fff;font-size:5.2px;letter-spacing:.04em}
.intro .sub{font-size:3.4px;margin-top:1px}
.block{position:absolute;font-size:1.7px;line-height:2.4px;color:#888}
.band{position:absolute;left:0;right:0}
.slide-h{position:absolute;left:5px;top:4px;font-family:'Montserrat',sans-serif;font-weight:500;font-size:4.2px;color:var(--navy)}
.slide-s{position:absolute;left:5px;top:9px;font-size:1.9px;color:var(--gold)}
.script{font-family:'Great Vibes',cursive;color:#555}
.disc{position:absolute;border-radius:50%}
</style>
</head>
<body>

<div class="intro">
  <div class="wordmark">Brennor Global</div>
  <div class="sub">Stationary Concepts</div>
</div>

<!-- business cards -->
<div class="piece navy" style="left:6px;top:57px;width:48px;height:27px">
  <div class="center wordmark" style="top:10px;font-size:3.6px">Brennor Global</div>
  <div class="center tiny" style="bottom:2px">www.brennorglbl.com</div>
  <div class="caption">Back Card Option_01</div>
</div>
<div class="piece" style="left:59px;top:57px;width:48px;height:27px">
  <div class="center wordmark" style="top:4px;font-size:4px">Brennor Global</div>
  <div class="center" style="top:10px;font-size:2.2px;font-weight:600;color:var(--navy)">Kiran Velur</div>
  <div class="center tiny" style="top:12.6px">CEO · M.S. Industrial Engineering (USA)</div>
  <div class="center tiny" style="top:15.4px">112 Kovirath Industrial Estate, Tarunpeth,<br>Ahmedabad 380119. India<br>+91 79 4410 2286 · info@brennorglbl.com</div>
  <div class="band" style="bottom:0;height:2px;background:var(--navy)"></div>
  <div class="caption">Front Card Option_01</div>
</div>
<div class="piece" style="left:6px;top:90px;width:48px;height:27px">
  <div class="center wordmark" style="top:10px;font-size:3.6px">Brennor Global</div>
  <div class="center tiny" style="bottom:2px;color:var(--navy)">www.brennorglbl.com</div>
  <div class="caption">Back Card Option_02</div>
</div>
<div class="piece" style="left:59px;top:90px;width:48px;height:27px">
  <div class="wordmark" style="position:absolute;left:3px;top:11px;font-size:2.8px">Brennor Global</div>
  <div style="position:absolute;left:24px;top:4px;width:.3px;height:19px;background:var(--rule)"></div>
  <div style="position:absolute;left:26px;top:4px;font-size:2px;font-weight:600;color:var(--navy)">Kiran Velur</div>
  <div class="tiny" style="position:absolute;left:26px;top:6.6px;width:21px">CEO<br>M.S. Industrial Engg. (USA)<br>+91 79 4410 2286<br>+91 98765 20417<br>info@brennorglbl.com</div>
  <div class="caption">Front Card Option_02</div>
</div>

<!-- letterheads -->
<div class="piece" style="left:109px;top:15px;width:78px;height:101px">
  <div class="wordmark" style="position:absolute;left:6px;top:7px;font-size:3.4px">Brennor Global</div>
  <div class="tiny" style="position:absolute;left:44px;top:6px;width:32px">112 Kovirath Industrial Estate<br>Tarunpeth, Ahmedabad 380119<br>info@brennorglbl.com</div>
  <div class="block" style="left:6px;top:22px;width:64px">Date<br>Recipient Name<br>Company Name<br>Street Address<br>City, State, Zip<br><br>We thank you for your interest in our export range and confirm that samples will ship this month. Our team remains available for any questions on pricing, lead times or packaging.<br><br>Kind regards,</div>
  <div role="img" aria-label="Handwritten signature" style="position:absolute;left:6px;top:62px;width:14px;height:4px;background:#d2d2dc"></div>
  <div class="block" style="left:6px;top:67px;color:var(--navy)">Kiran Velur</div>
  <div class="center tiny" style="bottom:3px;color:var(--navy)">www.brennorglbl.com</div>
  <div class="caption">Letterhead option_01</div>
</div>
<div class="piece" style="left:192px;top:15px;width:79px;height:101px">
  <div class="center wordmark" style="top:7px;font-size:3.4px">Brennor Global</div>
  <div class="block" style="left:6px;top:18px;width:66px">Date<br>Recipient Name<br>Company Name<br>Street Address<br><br>Please find enclosed our latest product catalogue and the updated price list. Delivery terms are FOB Mundra with standard export packing.<br><br>Sincerely,</div>
  <div role="img" aria-label="Handwritten signature" style="position:absolute;left:6px;top:52px;width:14px;height:4px;background:#d2d2dc"></div>
  <div class="block" style="left:6px;top:57px;color:var(--navy)">Kiran Velur</div>
  <div class="center tiny" style="bottom:3px">112 Kovirath Industrial Estate, Tarunpeth, Ahmedabad 380119 · +91 79 4410 2286 · info@brennorglbl.com</div>
  <div class="caption">Letterhead option_02</div>
</div>

<!-- envelopes -->
<div class="piece" style="left:276px;top:80px;width:84px;height:36px">
  <div class="wordmark" style="position:absolute;left:3px;top:3px;font-size:3px">Brennor Global</div>
  <div class="tiny" style="position:absolute;left:3px;top:7px">112 Kovirath Industrial Estate, Tarunpeth, Ahmedabad 380119</div>
  <div class="caption">Envelope Front</div>
</div>
<div class="piece" style="left:364px;top:40px;width:84px;height:76px;background:transparent;overflow:visible">
  <svg width="84" height="76" viewBox="0 0 84 76" style="position:absolute;left:0;top:0">
    <rect x="0" y="0" width="84" height="16" fill="var(--navy)"/>
    <rect x="0" y="20" width="84" height="22" fill="var(--gold)"/>
    <rect x="0" y="46" width="84" height="30" fill="#fff"/>
    <path d="M0 46 L42 60 L84 46" fill="none" stroke="#ddd" stroke-width=".4"/>
  </svg>
  <div class="center wordmark" style="top:5px;font-size:2.6px;color:#fff">Brennor Global</div>
  <div class="center wordmark" style="top:27px;font-size:2.6px;color:#fff">Brennor Global</div>
  <div class="center wordmark" style="top:62px;font-size:2.6px">Brennor Global</div>
  <div class="caption">Envelope Back</div>
</div>

<!-- folder -->
<div class="piece" style="left:466px;top:17px;width:122px;height:101px">
  <div style="position:absolute;left:0;top:0;width:4px;height:101px;background:var(--gold)"></div>
  <div style="position:absolute;left:4px;top:0;width:54px;height:101px;background:var(--navy)"></div>
  <div class="tiny" style="position:absolute;left:7px;top:58px;width:22px">112 Kovirath Industrial Estate, Tarunpeth, Ahmedabad 380119<br>info@brennorglbl.com</div>
  <div class="wordmark" style="position:absolute;left:74px;top:34px;font-size:3.4px">Brennor Global</div>
  <div style="position:absolute;right:0;top:0;width:4px;height:101px;background:var(--gold)"></div>
  <div style="position:absolute;left:58px;top:83px;width:60px;height:18px;background:var(--navy)"></div>
  <div class="caption">Folder</div>
</div>

<!-- fax sheets -->
<div class="piece" style="left:594px;top:15px;width:79px;height:101px">
  <div class="wordmark" style="position:absolute;left:5px;top:6px;font-size:3px">Brennor Global</div>
  <div class="block" style="left:5px;top:18px;width:70px">To: &nbsp; From:<br>Fax: &nbsp; Pages:<br>Phone: &nbsp; Date:<br>Re: &nbsp; CC:<br>Urgent · Review · Reply<br>Comments:</div>
  <div class="center tiny" style="bottom:3px">www.brennorglbl.com</div>
  <div class="caption">Fax option_01</div>
</div>
<div class="piece" style="left:677px;top:15px;width:79px;height:101px">
  <div class="center wordmark" style="top:6px;font-size:3px">Brennor Global</div>
  <div class="block" style="left:5px;top:18px;width:70px">To: &nbsp; From:<br>Fax: &nbsp; Pages:<br>Phone: &nbsp; Date:<br>Re: &nbsp; CC:<br>Urgent · Review · Reply<br>Comments:</div>
  <div class="center tiny" style="bottom:3px">+91 79 4410 2286 · info@brennorglbl.com</div>
  <div class="caption">Fax option_02</div>
</div>

<!-- compliment slip & thank you -->
<div class="piece" style="left:769px;top:28px;width:86px;height:36px">
  <div class="wordmark" style="position:absolute;left:4px;top:4px;font-size:3px">Brennor Global</div>
  <div class="tiny" style="position:absolute;left:52px;top:3px">112 Kovirath Industrial Estate<br>Ahmedabad 380119<br>info@brennorglbl.com</div>
  <div class="script center" style="top:19px;font-size:7px">With Compliments</div>
  <div class="caption">Compliment Slip</div>
</div>
<div class="piece" style="left:762px;top:73px;width:49px;height:38px">
  <div class="center wordmark" style="top:6px;font-size:3px">Brennor Global</div>
  <div class="script center" style="top:20px;font-size:6px">Thank you</div>
  <div class="caption">Thank You Card_Front</div>
</div>
<div class="piece navy" style="left:818px;top:73px;width:48px;height:38px">
  <div class="center wordmark" style="top:12px;font-size:3px;opacity:.35">Brennor Global</div>
  <div class="center tiny" style="bottom:3px">112 Kovirath Industrial Estate, Ahmedabad</div>
  <div class="caption">Thank You Card_Back</div>
</div>

<!-- CD and CD cover -->
<div class="disc" style="left:871px;top:7px;width:58px;height:58px;background:var(--navy)">
  <div class="center wordmark" style="top:9px;font-size:2.6px">Brennor Global</div>
  <div class="disc" style="left:21px;top:21px;width:16px;height:16px;background:#fff;border:1.5px solid #cfcfcf"></div>
  <div class="center tiny" style="bottom:10px">www.brennorglbl.com</div>
</div>
<div class="piece" style="left:934px;top:11px;width:58px;height:50px">
  <div class="band" style="top:0;height:3px;background:var(--navy)"></div>
  <div class="wordmark" style="position:absolute;left:4px;top:12px;font-size:2.8px">Brennor Global</div>
  <div class="center tiny" style="bottom:2px">112 Kovirath Industrial Estate · info@brennorglbl.com</div>
</div>

<!-- presentation -->
<div class="piece" style="left:1001px;top:13px;width:93px;height:70px">
  <div class="center wordmark" style="top:18px;font-size:6px">Brennor Global</div>
  <div class="center" style="top:43px;font-size:4px;color:var(--gold)">Welcome to Our</div>
  <div class="center" style="top:48px;font-size:5px;font-weight:600;color:var(--navy)">Presentation Name</div>
  <div class="center" style="top:55px;font-size:3.4px;color:var(--gold)">Description</div>
</div>
<div class="piece" style="left:1100px;top:13px;width:93px;height:70px">
  <div class="slide-h">Heading Here</div><div class="slide-s">Sub Heading</div>
  <div role="img" aria-label="Team member photo" style="position:absolute;left:6px;top:24px;width:18px;height:18px;background:#8a8a8a"></div>
  <div role="img" aria-label="Team member photo" style="position:absolute;left:27px;top:24px;width:18px;height:18px;background:#8a8a8a"></div>
  <div role="img" aria-label="Team member photo" style="position:absolute;left:48px;top:24px;width:18px;height:18px;background:#8a8a8a"></div>
  <div role="img" aria-label="Team member photo" style="position:absolute;left:69px;top:24px;width:18px;height:18px;background:#8a8a8a"></div>
  <div class="block" style="left:6px;top:45px;width:84px;color:var(--navy)">Team member1 &nbsp; Team member2 &nbsp; Team member3 &nbsp; Team member4</div>
</div>
<div class="piece" style="left:1001px;top:89px;width:93px;height:69px">
  <div class="slide-h">Heading Here</div><div class="slide-s">Sub Heading</div>
  <div class="block" style="left:5px;top:16px;width:40px"><b style="color:var(--navy)">Group1</b><br>Short note on this group.<br><b style="color:var(--navy)">Group2</b><br>Short note on this group.<br><b style="color:var(--navy)">Group3</b><br>Short note on this group.</div>
  <div class="block" style="left:48px;top:16px;width:40px"><b style="color:var(--navy)">Group4</b><br>Short note on this group.<br><b style="color:var(--navy)">Group5</b><br>Short note on this group.<br><b style="color:var(--navy)">Group6</b><br>Short note on this group.</div>
</div>
<div class="piece" style="left:1100px;top:89px;width:93px;height:69px">
  <div class="slide-h">Heading Here</div><div class="slide-s">Sub Heading</div>
  <svg width="46" height="40" viewBox="0 0 46 40" style="position:absolute;left:6px;top:16px">
    <line x1="0" y1="36" x2="46" y2="36" stroke="#bbb" stroke-width=".3"/>
    <rect x="8" y="10" width="4" height="26" fill="var(--navy)"/>
    <rect x="14" y="16" width="4" height="20" fill="var(--navy)"/>
    <rect x="20" y="8" width="4" height="28" fill="var(--navy)"/>
    <rect x="26" y="20" width="4" height="16" fill="var(--navy)"/>
    <rect x="32" y="14" width="4" height="22" fill="var(--navy)"/>
  </svg>
  <div class="block" style="left:58px;top:18px;width:32px">Sales rose steadily across the year with the best quarter in Q3.</div>
</div>
<div class="piece" style="left:1001px;top:165px;width:93px;height:70px">
  <div class="slide-h">Heading Here</div><div class="slide-s">Sub Heading</div>
  <div class="block" style="left:5px;top:16px;width:44px">Export volume is split across three regions, with the largest share going to Europe this season.</div>
  <svg width="26" height="26" viewBox="0 0 26 26" style="position:absolute;left:58px;top:20px">
    <circle cx="13" cy="13" r="12" fill="var(--navy)"/>
    <path d="M13 13 L13 1 A12 12 0 0 1 25 13 Z" fill="var(--gold)"/>
  </svg>
</div>
<div class="piece navy" style="left:1100px;top:165px;width:93px;height:70px">
  <div class="center" style="top:22px;font-size:13px;font-weight:400;color:#fff;font-family:'Montserrat',sans-serif">Thanks</div>
  <div class="center" style="top:38px;font-size:7px;color:#fff;font-family:'Montserrat',sans-serif">For Coming</div>
  <div class="center tiny" style="bottom:3px">112 Kovirath Industrial Estate · info@brennorglbl.com</div>
</div>

<!-- folder inner, magnets, CDs, covers -->
<div class="piece" style="left:475px;top:138px;width:124px;height:75px">
  <div class="center wordmark" style="top:28px;font-size:9px;opacity:.08">Brennor Global</div>
  <div style="position:absolute;left:0;top:0;width:3px;height:75px;background:var(--gold)"></div>
  <div style="position:absolute;right:0;top:0;width:3px;height:75px;background:var(--gold)"></div>
  <div style="position:absolute;left:9px;top:46px;width:106px;height:29px;background:var(--navy)"></div>
  <div class="caption">Folder Inner</div>
</div>
<div class="disc" style="left:484px;top:222px;width:22px;height:22px;background:#fff;border:1px solid var(--gold)"><div class="center wordmark" style="top:9px;font-size:1.7px">Brennor Global</div></div>
<div class="disc" style="left:510px;top:222px;width:22px;height:22px;background:var(--navy)"><div class="center wordmark" style="top:9px;font-size:1.7px;color:#fff">Brennor Global</div></div>
<div class="disc" style="left:536px;top:222px;width:22px;height:22px;background:var(--gold)"><div class="center wordmark" style="top:9px;font-size:1.7px;color:#fff">Brennor Global</div></div>
<div class="disc" style="left:562px;top:222px;width:22px;height:22px;background:#fff;border:1px solid var(--navy)"><div class="center wordmark" style="top:9px;font-size:1.7px">Brennor Global</div></div>

<div class="disc" style="left:682px;top:128px;width:58px;height:58px;background:var(--navy)"><div class="center wordmark" style="top:10px;font-size:2.6px">Brennor Global</div><div class="disc" style="left:21px;top:21px;width:16px;height:16px;background:#fff"></div></div>
<div class="disc" style="left:747px;top:128px;width:58px;height:58px;background:var(--gold)"><div class="center wordmark" style="top:10px;font-size:2.6px">Brennor Global</div><div class="disc" style="left:21px;top:21px;width:16px;height:16px;background:#fff"></div></div>
<div class="disc" style="left:682px;top:190px;width:58px;height:58px;background:#fff;border:1.5px solid var(--navy)"><div class="center wordmark" style="top:10px;font-size:2.6px">Brennor Global</div><div class="disc" style="left:20px;top:20px;width:16px;height:16px;background:#fff;border:1.5px solid #222"></div></div>
<div class="disc" style="left:747px;top:190px;width:58px;height:58px;background:var(--navy);border:1.5px solid #fff"><div class="center wordmark" style="top:10px;font-size:2.6px">Brennor Global</div><div class="disc" style="left:20px;top:20px;width:16px;height:16px;background:#fff"></div></div>

<div class="piece navy" style="left:820px;top:143px;width:57px;height:40px">
  <div class="wordmark" style="position:absolute;left:4px;top:4px;font-size:2.6px">Brennor Global</div>
  <div class="center tiny" style="bottom:2px">112 Kovirath Industrial Estate · info@brennorglbl.com</div>
</div>
<div class="piece" style="left:820px;top:195px;width:57px;height:40px">
  <div class="wordmark" style="position:absolute;left:4px;top:4px;font-size:2.6px">Brennor Global</div>
  <div class="center tiny" style="bottom:2px">112 Kovirath Industrial Estate · info@brennorglbl.com</div>
</div>

</body>
</html>
```